Industrial Services company needs a business card design

We provide industrial maintenance services including sandblasting, painting, pressure washing, storage tank rehabilitation, and welding. I would like an industrial design that's eye catching. I would like the back-side of the card to list our services.

Industry/Entity Type

Construction

Contact Information for Business Card

address: 418 Hartwell Lane, York, PA 17405
Phone: 410-637-4815
email: corvethinc@mailbrook.net
Daniel Verhoeven, President
www.corvethcoating.net

Logo Text

Corveth Industrial Services

Font styles to use
Sans Serif

Colors
000000
229ed3
0692cd
ffffff

Requirements
Must have
• Easy to read
• our services listed/included on back of card
• eye catching color combinations
Nice to have
• Water storage tank image

```html
<!DOCTYPE html>
<html lang="en">
<head>
<meta charset="utf-8">
<title>Corveth Industrial Services – Business Card</title>
<link href="https://fonts.googleapis.com/css2?family=Jost:wght@400;500;600&family=Montserrat:wght@600;700;800&display=swap" rel="stylesheet">
<style>
  :root {
    --black: #000000;
    --band-blue: #2f8fce;
    --bright-blue: #229ed3;
    --deep-blue: #0692cd;
    --white: #ffffff;
    --slate: #272d35;
    --splash-dark: #2a2fa8;
    --splash-mid: #1f5fc4;
    --splash-light: #1f8fd0;
  }
  * { box-sizing: border-box; margin: 0; padding: 0; }
  html, body { width: 831px; height: 1200px; overflow: hidden; background: var(--white); }
  body { position: relative; font-family: "Jost", sans-serif; color: var(--white); }

  .side-label {
    position: absolute; left: 0; width: 831px; text-align: center;
    font-family: "Jost", sans-serif; font-weight: 400; font-size: 40px; color: var(--black);
    line-height: 1;
  }
  .side-label--front { top: 4px; }
  .side-label--back { top: 636px; }

  .card { position: absolute; background: var(--black); overflow: hidden; }
  .card--front { left: 4px; top: 94px; width: 827px; height: 504px; }
  .card--back { left: 0; top: 692px; width: 829px; height: 508px; }

  .band { position: absolute; left: 0; width: 100%; background: var(--band-blue); }
  .card--front .band--top { top: 0; height: 42px; }
  .card--front .band--bottom { bottom: 0; height: 39px; display: flex; align-items: center; justify-content: center; }
  .band__url { font-family: "Jost", sans-serif; font-weight: 500; font-size: 30px; letter-spacing: 0.5px; color: var(--white); }

  .hero-art {
    position: absolute; left: 10px; top: 100px; width: 805px; height: 312px;
    background: radial-gradient(ellipse at 50% 50%, var(--splash-mid) 0%, var(--splash-dark) 55%, rgba(42, 47, 168, 0) 72%),
                linear-gradient(90deg, rgba(31, 143, 208, 0.35), rgba(42, 47, 168, 0.35));
  }

  .wordmark {
    position: absolute; left: 0; width: 100%; top: 310px; text-align: center;
    font-family: "Montserrat", sans-serif; font-weight: 800; font-size: 78px; letter-spacing: 6px;
    color: var(--white); line-height: 1;
  }

  .card--back .band--top { top: 0; height: 41px; }
  .slate-band { position: absolute; left: 0; top: 338px; width: 100%; height: 119px; background: var(--slate); }

  .person { position: absolute; left: 75px; top: 77px; }
  .person__name { font-family: "Jost", sans-serif; font-size: 41px; line-height: 1; color: var(--bright-blue); font-weight: 400; letter-spacing: 0.5px; }
  .person__name strong { font-weight: 600; }
  .person__title { font-family: "Jost", sans-serif; font-size: 30px; line-height: 1; margin-top: 5px; font-weight: 400; letter-spacing: 0.5px; }

  .contact { position: absolute; left: 78px; width: 378px; height: 51px; border: 3px solid var(--bright-blue);
    display: flex; align-items: center; padding-left: 12px; gap: 12px; font-size: 19px; font-weight: 400; }
  .contact svg { width: 20px; height: 20px; flex: none; fill: var(--white); }
  .contact--email { top: 168px; }
  .contact--phone { top: 243px; }
  .contact--address { top: 317px; }
  .contact--web { top: 390px; }

  .services { position: absolute; left: 504px; top: 168px; width: 293px; height: 274px; border: 3px solid var(--bright-blue);
    padding: 8px 0 0 10px; font-family: "Montserrat", sans-serif; }
  .services__title { font-size: 29px; font-weight: 700; line-height: 1.1; }
  .services__list { list-style: none; margin-top: 6px; }
  .services__list li { font-size: 18px; font-weight: 600; height: 47.5px; line-height: 1.2; }
</style>
</head>
<body>
  <div class="side-label side-label--front">FRONT</div>

  <section class="card card--front">
    <div class="band band--top"></div>
    <div class="hero-art" role="img" aria-label="Blue paint splash artwork behind the company name"></div>
    <div class="wordmark">CORVETH</div>
    <div class="band band--bottom"><span class="band__url">www.corvethcoating.net</span></div>
  </section>

  <div class="side-label side-label--back">BACK</div>

  <section class="card card--back">
    <div class="band band--top"></div>
    <div class="slate-band"></div>

    <div class="person">
      <h1 class="person__name">DANIEL <strong>VERHOEVEN</strong></h1>
      <p class="person__title">PRESIDENT</p>
    </div>

    <div class="contact contact--email">
      <svg viewBox="0 0 24 24" aria-hidden="true"><path d="M2 5h20v14H2z M4 7v1l8 5 8-5V7l-8 5z" fill-rule="evenodd"/></svg>
      <span>corvethinc@mailbrook.net</span>
    </div>
    <div class="contact contact--phone">
      <svg viewBox="0 0 24 24" aria-hidden="true"><path d="M6.6 10.8a15 15 0 0 0 6.6 6.6l2.2-2.2c.3-.3.7-.4 1-.2 1.1.4 2.3.6 3.6.6.6 0 1 .4 1 1V20c0 .6-.4 1-1 1A17 17 0 0 1 3 4c0-.6.4-1 1-1h3.5c.6 0 1 .4 1 1 0 1.3.2 2.5.6 3.6.1.3 0 .7-.2 1z"/></svg>
      <span>410-637-4815</span>
    </div>
    <div class="contact contact--address">
      <svg viewBox="0 0 24 24" aria-hidden="true"><path d="M12 3 2 12h3v8h5v-6h4v6h5v-8h3z"/></svg>
      <span>418 Hartwell Lane, York, PA 17405</span>
    </div>
    <div class="contact contact--web">
      <svg viewBox="0 0 24 24" aria-hidden="true"><circle cx="12" cy="12" r="9" fill="none" stroke="#fff" stroke-width="2"/><path d="M3 12h18M12 3c3 3 3 15 0 18M12 3c-3 3-3 15 0 18" fill="none" stroke="#fff" stroke-width="1.6"/></svg>
      <span>www.corvethcoating.net</span>
    </div>

    <div class="services">
      <h2 class="services__title">Our Services</h2>
      <ul class="services__list">
        <li>Sandblasting</li>
        <li>Industrial Painting</li>
        <li>Pressure washing</li>
        <li>Welding</li>
        <li>Storage tank services</li>
      </ul>
    </div>
  </section>
</body>
</html>
```